Web Site - Holloway-Strength.com

Design a 3 page web site for Holloway Strength. See attached design brief.
Holloway Strength - Web Site
www.holloway-strength.com

Design a 3 page web site for Holloway Strength, a small local fitness center that provided cardio and weights only (machines and free weights). There are no classes or other services offered at this facility. Holloway Strength is an affordable alternative to the big box, expensive fitness centers. It is small, local, convenient and a community oriented place to work out.
web site can be clean, simple and communicate basic information about the company and membership offers. Although the branding is black, orange and gray, the web site colors should be soft, light and neutral colors that will appeal to both men and women.
Text: Input generic text during design for each text area that will be modified later during the coding phase. The selected designer is expected to code the site and deliver all compressive files (images, files and code) for an unrestricted hand off and full ownership of all content by the client for future modifications by others.

Images
Images used can be generic royalty free images of people working out, on cardio machines, lifting on universal equipment, stretching or lifting weights or images with out people i.e a yoga mat, free weights, a row of cardio machines etc. This is an adults only facility - images can be a mix of men and women and of diverse multi ethnic backgrounds. Image of the actual gym are included below but should NOT be used on the web site.

Branding - See attached for vertical and horizontal logos for Holloway Strength. These can be used in any way and should be incorporated into the web site
WEB SITE OUTLINE
THREE web pages - Pages can be individual pages clicked through to each page from a navigation area but ALSO pages can be “blend together” into one long scrolling “home” or primary landing page.
1) Home Page with basic information
2) Membership Page (to be later integrated with Quillmark member software to show changing membership specials). - see example below - all text will change later
3) contact page - address - telephone number - google map directions
www.holloway-strength.com
Address:
Located in Tannery Brook Commons
418 E. Walnut Lane, Suite 305, Alderwick PA 18990
Tel: 484-555-0172

Target Market(s)

Men and Women - Adults over 18,

Industry/Entity Type

Fitness, Work Out, Gym

Coding

Coded - Design and coding required

Number of Pages Required

3 page

Requirements
Must have
• See Project Brief
Should not have
• Dark Colors that feel too masculine

```html
<!DOCTYPE html>
<html lang="en">
<head>
<meta charset="UTF-8">
<title>Holloway Strength</title>
<link href="https://fonts.googleapis.com/css2?family=Poppins:wght@300;400;500;600;700&display=swap" rel="stylesheet">
<style>
:root{
  --orange:#f59a4e;
  --orange-deep:#ef8431;
  --ink:#1f1f1f;
  --body:#4b4b4b;
  --cream:#faf6f1;
  --sand:#ece8e1;
  --card-sand:#e3ddd1;
  --card-light:#f4f2ee;
  --charcoal:#4a4a4a;
  --white:#ffffff;
}
*{box-sizing:border-box;margin:0;padding:0}
html,body{width:1200px;height:3396px;overflow:hidden}
body{font-family:'Poppins',sans-serif;color:var(--body);background:var(--cream);position:relative}
.section{position:absolute;left:0;width:1200px}

/* header */
.site-header{top:0;height:112px;background:var(--white);display:flex;align-items:center;padding:0 120px;z-index:2}
.brand{display:flex;align-items:center;gap:12px;font-weight:700;font-size:28px;color:var(--ink);letter-spacing:.5px;white-space:nowrap}
.brand-mark{width:22px;height:22px;background:var(--orange)}
.main-nav{margin-left:auto;display:flex;align-items:center;gap:28px;font-size:14px;font-weight:500;color:var(--ink);white-space:nowrap}
.btn{display:inline-block;background:var(--orange);color:var(--white);font-weight:600;font-size:13px;padding:14px 26px;border-radius:26px;letter-spacing:.5px;white-space:nowrap}
.call{display:flex;align-items:center;gap:12px;margin-left:18px;white-space:nowrap}
.icon-circle{flex:none;width:44px;height:44px;border-radius:50%;background:var(--white);display:flex;align-items:center;justify-content:center;box-shadow:0 2px 8px rgba(0,0,0,.12)}
.call-label{font-size:11px;color:var(--orange)}
.call-number{font-size:17px;font-weight:600;color:var(--ink)}

/* hero */
.hero{top:112px;height:568px;background:linear-gradient(180deg,#c9ccce 0%,#9ea3a6 40%,#55585b 100%)}
.hero-overlay{position:absolute;inset:0;background:linear-gradient(180deg,rgba(0,0,0,0) 35%,rgba(0,0,0,.55) 100%)}
.hero-text{position:absolute;left:120px;top:370px;color:var(--white);font-size:46px;line-height:1.2;letter-spacing:1px}
.hero-text .light{font-weight:300;display:block}
.hero-text .bold{font-weight:700;display:block}

/* about */
.about{top:680px;height:760px;background:var(--cream)}
.about-photo{position:absolute;left:144px;top:120px;width:416px;height:384px;background:linear-gradient(135deg,#8c8f92,#c4c2bd 60%,#6f7174)}
.about-copy{position:absolute;left:616px;top:150px;width:480px}
.about-copy h2{font-size:30px;font-weight:400;color:var(--ink);letter-spacing:1px;margin-bottom:30px;white-space:nowrap}
.about-copy h2 b{font-weight:700}
.about-copy p{font-size:14px;line-height:1.75;margin-bottom:34px;width:440px}
.about-actions{display:flex;align-items:center;gap:40px}
.about-note{position:absolute;left:300px;top:580px;width:600px;text-align:center;font-size:14px;line-height:1.75}

/* membership */
.membership{top:1440px;height:840px;background:linear-gradient(180deg,var(--sand),#e8e4dd)}
.section-title{text-align:center;font-size:42px;font-weight:400;color:var(--ink);letter-spacing:1px}
.section-title b{font-weight:700}
.membership .section-title{margin-top:90px}
.section-sub{width:760px;margin:22px auto 0;text-align:center;font-size:14px;line-height:1.7}
.plans{position:absolute;top:260px;left:208px;display:flex;gap:60px}
.plan{position:relative;width:360px;height:500px;border-radius:14px;padding:150px 44px 0;box-shadow:0 10px 30px rgba(0,0,0,.08)}
.plan.signature{background:var(--card-sand)}
.plan.pro{background:var(--card-light)}
.plan-icon{position:absolute;top:36px;left:44px;width:70px;height:70px;border-radius:12px;background:rgba(245,154,78,.25);display:flex;align-items:center;justify-content:center}
.plan h3{font-size:18px;font-weight:600;color:var(--ink);margin-bottom:22px}
.plan p{font-size:14px;line-height:1.75;margin-bottom:30px}
.price{font-size:32px;font-weight:500;color:var(--ink);margin-bottom:18px}
.price span{font-size:18px}
.more{font-size:13px;font-weight:500;color:var(--ink);text-decoration:underline}

/* testimonials */
.testimonials{top:2280px;height:700px;background:linear-gradient(180deg,#f2f0ed,#e7e3de)}
.testimonials .section-title{margin-top:100px}
.reviews{position:absolute;top:230px;left:144px;display:flex;gap:48px}
.review{width:270px}
.review-head{display:flex;align-items:center;gap:16px;margin-bottom:18px}
.avatar{width:72px;height:72px;border-radius:50%;background:linear-gradient(135deg,#b9a898,#7d6d62)}
.review-name{font-size:14px;font-weight:600;color:var(--ink)}
.review-role{font-size:12px}
.review p{font-size:13px;line-height:1.7}

/* footer */
.site-footer{top:2980px;height:416px;background:var(--charcoal);color:var(--white)}
.cta{position:absolute;left:148px;top:2840px;width:904px;height:320px;background:var(--orange);color:var(--white);text-align:center;padding-top:56px;z-index:2}
.cta h2{font-size:40px;font-weight:400;line-height:1.2;letter-spacing:1px}
.cta h2 b{font-weight:700;display:block}
.cta p{width:600px;margin:18px auto 26px;font-size:14px;line-height:1.6}
.btn.dark{background:var(--charcoal)}
.footer-row{position:absolute;top:220px;left:150px;right:120px;display:flex;align-items:center}
.footer-nav{display:flex;gap:28px;font-size:14px;font-weight:500;white-space:nowrap}
.copyright{font-size:12px;margin-top:14px;opacity:.85;white-space:nowrap}
.footer-info{display:flex;align-items:center;gap:16px;margin-left:90px;white-space:nowrap}
.footer-info + .footer-info{margin-left:60px}
.footer-info .label{font-size:12px;opacity:.85}
.footer-info .value{font-size:17px;font-weight:600}
.footer-info .addr{font-size:12px;font-weight:600;line-height:1.5}
</style>
</head>
<body>

<header class="section site-header">
  <div class="brand"><span class="brand-mark"></span>Holloway Strength</div>
  <nav class="main-nav">
    <span>HOME</span>
    <span>MEMBERSHIP</span>
    <span class="btn">CONTACT US</span>
    <div class="call">
      <span class="icon-circle"><svg width="20" height="20" viewBox="0 0 24 24"><path d="M6.6 10.8a15.2 15.2 0 0 0 6.6 6.6l2.2-2.2a1 1 0 0 1 1-.25 11.4 11.4 0 0 0 3.6.57 1 1 0 0 1 1 1V20a1 1 0 0 1-1 1A17 17 0 0 1 3 4a1 1 0 0 1 1-1h3.5a1 1 0 0 1 1 1c0 1.25.2 2.45.57 3.57a1 1 0 0 1-.25 1z" fill="#1f1f1f"/></svg></span>
      <div><div class="call-label">Call us Today</div><div class="call-number">484-555-0172</div></div>
    </div>
  </nav>
</header>

<section class="section hero" role="img" aria-label="Bright gym floor with rows of cardio machines in front of large windows overlooking mountains">
  <div class="hero-overlay"></div>
  <h1 class="hero-text"><span class="light">FITNESS MADE SIMPLE.</span><span class="bold">BUILT FOR YOUR ROUTINE.</span></h1>
</section>

<section class="section about">
  <div class="about-photo" role="img" aria-label="Gym interior with treadmills facing tall windows"></div>
  <div class="about-copy">
    <h2>ABOUT <b>HOLLOWAY STRENGTH</b></h2>
    <p>Holloway Strength is a small, local gym built for people who want a simple place to train. We offer cardio machines, selectable weight equipment and a full free weight area, with friendly staff and no crowds. Come in, warm up, and work at your own pace every day.</p>
    <div class="about-actions">
      <span class="btn">CONTACT US</span>
      <div class="call">
        <span class="icon-circle"><svg width="20" height="20" viewBox="0 0 24 24"><path d="M6.6 10.8a15.2 15.2 0 0 0 6.6 6.6l2.2-2.2a1 1 0 0 1 1-.25 11.4 11.4 0 0 0 3.6.57 1 1 0 0 1 1 1V20a1 1 0 0 1-1 1A17 17 0 0 1 3 4a1 1 0 0 1 1-1h3.5a1 1 0 0 1 1 1c0 1.25.2 2.45.57 3.57a1 1 0 0 1-.25 1z" fill="#1f1f1f"/></svg></span>
        <div><div class="call-label">Call us Today</div><div class="call-number">484-555-0172</div></div>
      </div>
    </div>
  </div>
  <p class="about-note">No classes, no long contracts and no pressure. Just clean equipment, fair prices and a community that shows up for each other. Stop by for a tour and see how easy it is to stay consistent.</p>
</section>

<section class="section membership">
  <h2 class="section-title">MEMBERSHIP <b>PLAN</b></h2>
  <p class="section-sub">Simple monthly plans with full access to cardio and strength equipment. Pick the one that fits your schedule and start training this week.</p>
  <div class="plans">
    <article class="plan signature">
      <span class="plan-icon"><svg width="34" height="34" viewBox="0 0 24 24" fill="none" stroke="#ef8431" stroke-width="1.6"><rect x="3" y="5" width="18" height="14" rx="2"/><path d="M3 10h18M7 15h4"/></svg></span>
      <h3>SIGNATURE MEMBERSHIP</h3>
      <p>Full access to cardio machines and the weight floor during staffed hours, a locker room, free fitness assessment and one guest pass each month.</p>
      <div class="price">$ 199 <span>/Month</span></div>
      <span class="more">Explore More Details</span>
    </article>
    <article class="plan pro">
      <span class="plan-icon"><svg width="34" height="34" viewBox="0 0 24 24" fill="none" stroke="#ef8431" stroke-width="1.6"><path d="M6 4h12v5a6 6 0 0 1-12 0z"/><path d="M12 15v4M8 21h8"/></svg></span>
      <h3>PRO MEMBERSHIP</h3>
      <p>Everything in Signature plus key fob entry around the clock, two guest passes a month, towel service and a quarterly progress check with staff.</p>
      <div class="price">$ 199 <span>/Month</span></div>
      <span class="more">Explore More Details</span>
    </article>
  </div>
</section>

<section class="section testimonials">
  <h2 class="section-title">OUR <b>TESTIMONIALS</b></h2>
  <div class="reviews">
    <article class="review">
      <div class="review-head"><span class="avatar" role="img" aria-label="Portrait of member Dana Reyes"></span><div><div class="review-name">DANA REYES</div><div class="review-role">Member Since 2021</div></div></div>
      <p>Quiet, clean and never crowded. I finally have a gym where I can get in, finish my routine and get on with my day.</p>
    </article>
    <article class="review">
      <div class="review-head"><span class="avatar" role="img" aria-label="Portrait of member Marcus Bell"></span><div><div class="review-name">MARCUS BELL</div><div class="review-role">Member Since 2021</div></div></div>
      <p>The staff know my name and the weight area always has what I need. Best value I have found anywhere nearby.</p>
    </article>
    <article class="review">
      <div class="review-head"><span class="avatar" role="img" aria-label="Portrait of member Priya Nair"></span><div><div class="review-name">PRIYA NAIR</div><div class="review-role">Member Since 2021</div></div></div>
      <p>Friendly and welcoming from day one. The cardio machines are well kept and I never wait for a treadmill.</p>
    </article>
  </div>
</section>

<div class="cta">
  <h2>FIND THE MEMBERSHIP THAT <b>FITS YOUR ROUTINE</b></h2>
  <p>Simple, affordable memberships for adults who want a local gym that respects their time and budget.</p>
  <span class="btn dark">GET MEMBERSHIP</span>
</div>

<footer class="section site-footer">
  <div class="footer-row">
    <div>
      <div class="footer-nav"><span>HOME</span><span>MEMBERSHIP</span><span>CONTACT US</span></div>
      <div class="copyright">Copyright©2025 All Rights Reserved</div>
    </div>
    <div class="footer-info">
      <span class="icon-circle"><svg width="20" height="20" viewBox="0 0 24 24"><path d="M6.6 10.8a15.2 15.2 0 0 0 6.6 6.6l2.2-2.2a1 1 0 0 1 1-.25 11.4 11.4 0 0 0 3.6.57 1 1 0 0 1 1 1V20a1 1 0 0 1-1 1A17 17 0 0 1 3 4a1 1 0 0 1 1-1h3.5a1 1 0 0 1 1 1c0 1.25.2 2.45.57 3.57a1 1 0 0 1-.25 1z" fill="#1f1f1f"/></svg></span>
      <div><div class="label">Call us Today</div><div class="value">484-555-0172</div></div>
    </div>
    <div class="footer-info">
      <span class="icon-circle"><svg width="20" height="20" viewBox="0 0 24 24"><path d="M12 2a7 7 0 0 0-7 7c0 5 7 13 7 13s7-8 7-13a7 7 0 0 0-7-7zm0 9.5A2.5 2.5 0 1 1 12 6.5a2.5 2.5 0 0 1 0 5z" fill="#1f1f1f"/></svg></span>
      <div><div class="label">Location</div><div class="addr">Tannery Brook Commons, 418 E. Walnut Lane<br>Suite 305, Alderwick PA 18990</div></div>
    </div>
  </div>
</footer>

</body>
</html>
```